TR Stationery - Modern Contemporary

Develop modern template for Letterhead and Stationery (business card, letterhead, envelopes) using the TR Logo and Icon

Colors
0054AA
0677BA
7BADD7
CADEEF
E8F1F8
00AB8E
00BBA5
67D7C9
C6EFE9
E9F9F6
EE7325
F08F49
F5BC92
FAE3D3
FDF4ED
6B429C
8869AF
B7A5CE
E3DAEB
F3F0F8

```html
<!DOCTYPE html>
<html lang="en">
<head>
<meta charset="utf-8">
<title>TR Stationery – Business Card</title>
<link rel="stylesheet" href="https://fonts.googleapis.com/css2?family=Playfair+Display:wght@500&family=Arimo:wght@400&display=swap">
<style>
  :root {
    --backdrop: #1c1c1e;
    --card: #121b26;
    --white: #ffffff;
    --green: #00ab8e;
    --orange: #ee7325;
    --rule: #5a6572;
  }
  * { box-sizing: border-box; margin: 0; padding: 0; }
  html, body {
    width: 1200px;
    height: 900px;
    overflow: hidden;
    background: var(--backdrop);
  }
  .sheet {
    position: relative;
    width: 1200px;
    height: 900px;
  }
  .card {
    position: absolute;
    width: 560px;
    height: 320px;
    border-radius: 22px;
    background: var(--card);
    box-shadow: 0 18px 40px rgba(0,0,0,.45);
  }
  .card--front { left: 320px; top: 90px; }
  .card--back  { left: 320px; top: 490px; }

  .brand-name {
    font-family: "Arimo", sans-serif;
    font-weight: 400;
    color: var(--white);
    white-space: nowrap;
  }
  .card--front .brand-name {
    position: absolute;
    left: 48px; top: 140px;
    font-size: 34px;
    line-height: 40px;
  }
  .card--back .brand-name {
    position: absolute;
    left: 0; right: 0; top: 132px;
    text-align: center;
    font-size: 48px;
    line-height: 56px;
  }

  .divider {
    position: absolute;
    left: 300px; top: 70px;
    width: 1px; height: 180px;
    background: var(--rule);
  }
  .contact {
    position: absolute;
    left: 322px; top: 76px;
    font-family: "Arimo", sans-serif;
    color: var(--white);
  }
  .contact__name {
    font-family: "Playfair Display", serif;
    font-weight: 500;
    font-size: 21px;
    color: var(--green);
    line-height: 1;
  }
  .contact__title {
    font-size: 13px;
    color: var(--orange);
    margin-top: 3px;
    margin-bottom: 14px;
  }
  .contact__list { list-style: none; }
  .contact__item {
    display: flex;
    align-items: center;
    gap: 8px;
    font-size: 13px;
    line-height: 19px;
  }
  .contact__icon { width: 12px; height: 12px; flex: none; }
  .contact__address {
    font-size: 13px;
    line-height: 17px;
    margin-top: 16px;
    padding-left: 20px;
  }
</style>
</head>
<body>
<main class="sheet">
  <section class="card card--front" aria-label="Business card, front">
    <p class="brand-name">tera rivo</p>
    <div class="divider"></div>
    <div class="contact">
      <p class="contact__name">Daniel Harper</p>
      <p class="contact__title">Managing Director</p>
      <ul class="contact__list">
        <li class="contact__item">
          <svg class="contact__icon" viewBox="0 0 24 24" aria-hidden="true"><path fill="var(--green)" d="M6.6 10.8a15.1 15.1 0 0 0 6.6 6.6l2.2-2.2c.3-.3.7-.4 1-.2 1.1.4 2.3.6 3.6.6.6 0 1 .4 1 1V20c0 .6-.4 1-1 1C10.6 21 3 13.4 3 4c0-.6.4-1 1-1h3.5c.6 0 1 .4 1 1 0 1.3.2 2.5.6 3.6.1.3 0 .7-.2 1z"/></svg>
          <span>044-310 552 874</span>
        </li>
        <li class="contact__item">
          <svg class="contact__icon" viewBox="0 0 24 24" aria-hidden="true"><rect x="2" y="5" width="20" height="14" rx="1.5" fill="var(--green)"/><path d="M2.5 6l9.5 7 9.5-7" fill="none" stroke="var(--card)" stroke-width="1.6"/></svg>
          <span>hello@terarivo.com</span>
        </li>
        <li class="contact__item">
          <svg class="contact__icon" viewBox="0 0 24 24" aria-hidden="true"><g fill="none" stroke="var(--green)" stroke-width="2"><circle cx="12" cy="12" r="9.5"/><ellipse cx="12" cy="12" rx="4.2" ry="9.5"/><path d="M2.5 12h19M4 7h16M4 17h16"/></g></svg>
          <span>www.terarivo.com</span>
        </li>
      </ul>
      <p class="contact__address">88 Harbour Lane, Suite 4<br>20931, Eastland</p>
    </div>
  </section>

  <section class="card card--back" aria-label="Business card, back">
    <p class="brand-name">tera rivo</p>
  </section>
</main>
</body>
</html>
```